Create a Awesome Email Banner - Promoting our LED Strip Lighting Range

Hi all,

We are an online lighting retailer and we need a stunning email banner. This will be used to promote to range of Bespoke, cut to size led strip lights.

It will point to this page:
brightvorn.co.uk/led-tape/led-tape-single-colour/led-tape-cut-to-size/
and also:
brightvorn.co.uk/led-tape/rgb-colour-changing-led-tape/

Email banner should be - 600x800px - + Shop Now Button

Banners should include the message "Bespoke, Cut to size LED Strip Lighting from only £14.95."

Please make sure that the banners match our website colour scheme. brightvorn.co.uk/

DO NOT INCLUDE OUR LOGO IN YOUR DESIGN

Please make your entry unique and creative and DO NOT copy other freelancers work.

If you have any questions then please use the clarification board but please DON'T use it to ask me to check your entry - ALL entries will be rated!

Thank you and GOOD LUCK!
(Dorvane)

```html
<!DOCTYPE html>
<html lang="en">
<head>
<meta charset="utf-8">
<title>LED Strip Lighting – Email Banner</title>
<link rel="stylesheet" href="https://fonts.googleapis.com/css2?family=Roboto+Condensed:wght@700&family=Arimo:wght@700&display=swap">
<style>
  :root {
    --bg: #000000;
    --frame: #ffffff;
    --accent-blue: #1ea5e9;
    --text-white: #ffffff;
    --button-red: #e3283d;
    --glow-blue: 52, 90, 255;
    --glow-green: 40, 220, 110;
    --glow-red: 255, 50, 70;
    --glow-violet: 170, 90, 255;
  }
  html, body {
    margin: 0;
    padding: 0;
    width: 900px;
    height: 1200px;
    overflow: hidden;
    background: var(--bg);
  }
  .banner {
    position: relative;
    width: 900px;
    height: 1200px;
    box-sizing: border-box;
    border: 3px solid var(--frame);
    background: var(--bg);
    overflow: hidden;
  }
  .product-visual {
    position: absolute;
    left: 0;
    top: 400px;
    width: 894px;
    height: 794px;
    background:
      radial-gradient(ellipse 16% 7% at 28% 8%, rgba(var(--glow-violet), 0.85), transparent 75%),
      radial-gradient(ellipse 20% 8% at 58% 6%, rgba(var(--glow-green), 0.7), transparent 75%),
      radial-gradient(ellipse 14% 14% at 10% 14%, rgba(var(--glow-blue), 0.8), transparent 75%),
      radial-gradient(ellipse 22% 14% at 30% 22%, rgba(var(--glow-red), 0.55), transparent 75%),
      radial-gradient(ellipse 12% 18% at 72% 22%, rgba(var(--glow-green), 0.7), transparent 75%),
      radial-gradient(ellipse 14% 20% at 84% 38%, rgba(var(--glow-red), 0.6), transparent 75%),
      radial-gradient(ellipse 26% 10% at 45% 33%, rgba(var(--glow-blue), 0.75), transparent 75%),
      radial-gradient(ellipse 22% 12% at 55% 45%, rgba(var(--glow-green), 0.6), transparent 75%),
      radial-gradient(ellipse 14% 22% at 18% 58%, rgba(var(--glow-blue), 0.8), transparent 75%),
      radial-gradient(ellipse 18% 14% at 62% 54%, rgba(var(--glow-red), 0.6), transparent 75%),
      radial-gradient(ellipse 24% 10% at 40% 70%, rgba(var(--glow-violet), 0.7), transparent 75%),
      radial-gradient(ellipse 16% 12% at 75% 66%, rgba(var(--glow-blue), 0.7), transparent 75%),
      radial-gradient(ellipse 20% 10% at 30% 82%, rgba(var(--glow-red), 0.55), transparent 75%),
      radial-gradient(ellipse 12% 22% at 90% 78%, rgba(var(--glow-green), 0.6), transparent 75%),
      radial-gradient(ellipse 60% 45% at 48% 45%, rgba(40, 40, 90, 0.55), transparent 80%),
      var(--bg);
  }
  .headline {
    position: absolute;
    inset: 0;
    margin: 0;
    font-weight: 700;
    line-height: 1;
  }
  .headline__line {
    position: absolute;
    left: 39px;
    white-space: nowrap;
  }
  .headline__tagline {
    top: 44px;
    font-family: "Roboto Condensed", sans-serif;
    font-size: 78px;
    color: var(--accent-blue);
  }
  .headline__product {
    top: 153px;
    left: 40px;
    font-family: "Arimo", sans-serif;
    font-size: 90px;
    color: var(--text-white);
    letter-spacing: -0.5px;
  }
  .headline__price {
    top: 276px;
    left: 44px;
    font-family: "Roboto Condensed", sans-serif;
    font-size: 90px;
    color: var(--accent-blue);
  }
  .headline__amount {
    color: var(--text-white);
  }
  .shop-button {
    position: absolute;
    left: 505px;
    top: 1030px;
    width: 352px;
    height: 122px;
    text-decoration: none;
  }
  .shop-button svg {
    position: absolute;
    inset: 0;
  }
  .shop-button__label {
    position: absolute;
    left: 150px;
    top: 20px;
    font-family: "Arimo", sans-serif;
    font-weight: 700;
    font-size: 40px;
    line-height: 1.05;
    color: var(--text-white);
    text-align: center;
  }
  .site-link {
    position: absolute;
    left: 32px;
    top: 1098px;
    display: flex;
    align-items: center;
    gap: 10px;
    font-family: "Arimo", sans-serif;
    font-weight: 700;
    font-size: 35px;
    color: var(--text-white);
  }
</style>
</head>
<body>
  <main class="banner">
    <div class="product-visual" role="img" aria-label="Coiled multicolour LED rope light glowing blue, green and red on a black surface"></div>

    <h1 class="headline">
      <span class="headline__line headline__tagline">Bespoke, Cut to size</span>
      <span class="headline__line headline__product">LED Strip Lighting</span>
      <span class="headline__line headline__price">From only <span class="headline__amount">£14.95.</span></span>
    </h1>

    <a class="shop-button" href="#">
      <svg width="352" height="122" viewBox="0 0 352 122" aria-hidden="true">
        <polygon points="8,8 345,0 352,112 0,122" fill="var(--button-red)"/>
        <g fill="none" stroke="var(--text-white)" stroke-width="6" stroke-linecap="round" stroke-linejoin="round">
          <path d="M30 38 H48 L62 84 H118 L128 52 H54"/>
          <line x1="66" y1="62" x2="124" y2="62"/>
          <line x1="80" y1="52" x2="80" y2="84"/>
          <line x1="100" y1="52" x2="100" y2="84"/>
        </g>
        <circle cx="70" cy="97" r="6" fill="var(--text-white)"/>
        <circle cx="110" cy="97" r="6" fill="var(--text-white)"/>
      </svg>
      <span class="shop-button__label">SHOP<br>NOW</span>
    </a>

    <div class="site-link">
      <svg width="60" height="60" viewBox="0 0 54 54" aria-hidden="true">
        <g fill="none" stroke="var(--text-white)" stroke-width="3">
          <circle cx="27" cy="27" r="24"/>
          <ellipse cx="27" cy="27" rx="11" ry="24"/>
          <line x1="27" y1="3" x2="27" y2="51"/>
          <line x1="3" y1="27" x2="51" y2="27"/>
          <path d="M7 15 H47 M7 39 H47"/>
        </g>
      </svg>
      <span class="site-link__url">www.brightvorn.co.uk</span>
    </div>
  </main>
</body>
</html>
```